Group training gym/bootcamp needs a web design

We need a website for our gym that is based in Sydney. We have indoor functional training classes and outdoor bootcamp classes. We would like the web site to have a video (to be created) and photo gallery. I would like the site made on word press and i would like to be able to make minor changes such as changing images and text without having to use a designer.

The website should have the following pages: home page; the gym; the bootcamp; photo gallery; about us; contact.

I have uploaded our logo and i would like to keep to these colour (blue,yellow,silver) and black is also allowed

Target Market(s)

18-50 male and female

Industry/Entity Type

Gym

Coding

Coded - Design and coding required

Number of Pages Required

5+ page

Font styles to use
Sans Serif

Colors
0692cd
fbed22
1b1b1b
e8e8e8

Requirements
Must have
• The website should have the following pages: home page; the gym; the bootcamp; photo gallery; about us; contact.
• I have uploaded our logo and i would like to keep to these colour (blue,yellow,silver) and black is also allowed
• Video upload and photo upload

```html
<!DOCTYPE html>
<html lang="en">
<head>
<meta charset="utf-8">
<title>Pulse Forge Fitness</title>
<link href="https://fonts.googleapis.com/css2?family=Audiowide&family=Roboto:wght@400;500;700&display=swap" rel="stylesheet">
<style>
:root{
  --blue:#0692cd;
  --yellow:#fbed22;
  --dark:#1b1b1b;
  --darker:#111111;
  --light:#e8e8e8;
  --white:#ffffff;
  --grey:#7a7a7a;
  --display:"Audiowide",sans-serif;
  --body:"Roboto",sans-serif;
}
*{box-sizing:border-box;margin:0;padding:0}
html,body{width:1200px;height:4772px;overflow:hidden;background:var(--dark)}
body{font-family:var(--body);color:var(--dark)}
.page{position:relative;width:1200px;height:4772px;overflow:hidden;background:var(--dark)}
.abs{position:absolute}
.shapes{position:absolute;left:0;top:0}
.photo{position:absolute}
.btn{position:absolute;display:block;background:var(--yellow);color:var(--dark);font:700 14px/40px var(--body);letter-spacing:1px;text-align:center;text-transform:uppercase;width:150px;height:40px}
.center-x{left:50%;transform:translateX(-50%)}

/* top bar & nav */
.topbar{position:absolute;left:0;top:0;width:1200px;height:32px;background:rgba(0,0,0,.55);color:var(--light);font:13px/32px var(--body);padding:0 40px;z-index:5}
.topbar .phone{float:left}
.topbar .social{float:right;display:flex;gap:10px;margin-top:11px}
.topbar .social i{display:block;width:10px;height:10px;border-radius:50%;background:var(--blue)}
.nav{position:absolute;left:0;top:32px;width:1200px;height:60px;z-index:5;display:flex;justify-content:center;align-items:center;gap:38px;font:500 14px var(--body);text-transform:uppercase;color:var(--white)}
.nav a{color:var(--white);text-decoration:none}
.nav a.active{color:var(--yellow);border-bottom:2px solid var(--yellow);padding-bottom:4px}
.brand{display:flex;align-items:center;gap:8px;padding:0 26px;font:18px var(--display);color:var(--yellow);text-transform:uppercase}
.brand i{display:block;width:34px;height:34px;border-radius:50%;background:var(--blue)}

/* hero */
.hero-photo{left:0;top:0;width:1200px;height:860px;background:radial-gradient(ellipse at 50% 30%,#4a4a4a 0%,#262626 45%,#111 100%)}
.hero-title{position:absolute;top:232px;width:1200px;text-align:center;font:40px var(--display);color:var(--yellow);text-transform:uppercase}
.hero-text{position:absolute;top:292px;left:370px;width:460px;text-align:center;font:14px/22px var(--body);color:var(--light)}
.slide-arrow{position:absolute;top:110px;width:22px;height:28px;background:var(--white);color:var(--dark);font:700 14px/28px var(--body);text-align:center}

/* section headings */
.eyebrow{position:absolute;width:1200px;text-align:center;font:20px var(--display);color:var(--blue);text-transform:uppercase}
.heading{position:absolute;width:1200px;text-align:center;font:32px var(--display);color:var(--blue);text-transform:uppercase}
.para{position:absolute;font:14px/22px var(--body);color:var(--grey)}

/* bootcamp */
.boot-kicker{left:240px;top:1060px;font:20px var(--display);color:var(--blue);text-transform:uppercase}
.boot-title{left:240px;top:1088px;font:34px var(--display);color:var(--blue);text-transform:uppercase}
.boot-lead{left:240px;top:1146px;width:440px;font:20px/28px var(--body);color:var(--dark)}
.boot-list{position:absolute;left:240px;top:1222px;list-style:none;font:500 14px/18px var(--body);color:var(--dark)}
.boot-list li{display:flex;align-items:flex-start;gap:12px;margin-bottom:14px;width:440px}
.boot-list svg{flex:none;margin-top:2px}
.price{position:absolute;left:240px;top:1452px;display:flex;align-items:center;height:72px}
.price .label{background:var(--white);font:500 18px/22px var(--body);color:var(--blue);padding:4px 14px;height:72px;display:flex;align-items:center;text-transform:uppercase}
.price .amount{background:var(--yellow);font:700 48px/72px var(--body);padding:0 20px;color:var(--dark)}

/* gallery */
.gallery{position:absolute;left:0;top:1852px;width:1200px;height:468px;display:grid;grid-template-columns:repeat(5,1fr);grid-template-rows:232px 232px;gap:4px;background:var(--dark)}
.gallery div{width:100%;height:100%}

/* video */
.section-title-y{position:absolute;width:1200px;text-align:center;font:32px var(--display);color:var(--yellow);text-transform:uppercase}
.video{position:absolute;left:248px;top:2690px;width:704px;height:380px;background:linear-gradient(180deg,#3a3a3a,#1e1e1e);border:4px solid #2b2b2b}
.video .tools{position:absolute;right:0;top:0;width:56px;height:100%;background:rgba(0,0,0,.6);display:flex;flex-direction:column;align-items:center;gap:22px;padding-top:18px}
.video .tools i{display:block;width:22px;height:20px;border:2px solid var(--white);border-radius:3px}
.video .bar{position:absolute;left:0;bottom:0;width:100%;height:40px;background:rgba(0,0,0,.75);display:flex;align-items:center;gap:14px;padding:0 16px;color:var(--white);font:700 12px var(--body)}
.video .track{flex:1;height:5px;background:#555;position:relative}
.video .track span{position:absolute;left:0;top:0;height:5px;width:22%;background:var(--blue)}

/* gym cards */
.gym-card{position:absolute;top:3180px;width:568px;height:220px;background:var(--yellow);overflow:hidden}
.gym-card .photo-side{position:absolute;right:0;top:0;width:230px;height:220px;background:linear-gradient(90deg,var(--yellow),#b7a628 60%,#5b5213)}
.gym-card h3{position:absolute;left:30px;top:30px;font:28px var(--display);color:var(--dark);text-transform:uppercase}
.gym-card p{position:absolute;left:30px;top:86px;width:330px;font:14px/22px var(--body);color:var(--dark)}

/* blog */
.blog-main{position:absolute;left:252px;top:3700px;width:340px;height:420px;background:linear-gradient(160deg,#6b6b6b,#2b2b2b)}
.blog-main .caption{position:absolute;left:14px;bottom:24px;width:170px;background:var(--yellow);padding:14px;font:20px/24px var(--display);color:var(--dark);text-transform:uppercase}
.blog-small{position:absolute;width:160px;height:200px;background:linear-gradient(160deg,#444,#1b1b1b)}
.blog-small p{position:absolute;left:12px;top:18px;width:90px;font:12px/15px var(--display);color:var(--yellow);text-transform:uppercase}

/* footer */
.foot-brand{position:absolute;top:4520px;width:1200px;display:flex;justify-content:center;align-items:center;gap:10px;font:26px var(--display);color:var(--yellow);text-transform:uppercase}
.foot-brand i{display:block;width:44px;height:44px;border-radius:50%;background:var(--blue)}
.footer{position:absolute;left:0;top:4600px;width:1200px;height:142px;background:var(--darker);display:flex;gap:60px;padding:20px 240px 0}
.footer h4{font:700 13px var(--body);color:var(--yellow);text-transform:uppercase;margin-bottom:10px}
.footer p,.footer li{font:12px/18px var(--body);color:#aaa;list-style:none}
.footer .col{width:220px}
.footer .contact li{display:flex;gap:8px;align-items:center}
.footer .contact i{width:8px;height:8px;background:var(--blue);display:block}
.copyright{position:absolute;left:0;top:4742px;width:1200px;height:30px;background:#000;color:#888;font:11px/30px var(--body);padding:0 240px;display:flex;justify-content:space-between}
.copyright span:last-child{color:var(--yellow)}
</style>
</head>
<body>
<div class="page">

  <!-- hero -->
  <div class="photo hero-photo" role="img" aria-label="Athlete training with weights in a dark gym"></div>
  <svg class="shapes" width="1200" height="1060" viewBox="0 0 1200 1060" aria-hidden="true">
    <polygon points="0,380 600,620 0,860" fill="#0692cd"/>
    <polygon points="1200,380 600,620 1200,860" fill="#0692cd"/>
    <polygon points="0,300 600,560 600,620 0,380" fill="#0b6f9b" opacity=".55"/>
    <polygon points="1200,300 600,560 600,620 1200,380" fill="#0b6f9b" opacity=".55"/>
    <polygon points="0,860 600,600 1200,860 1200,1060 0,1060" fill="#ffffff"/>
  </svg>

  <header>
    <div class="topbar"><span class="phone">+61 2 5550 0148</span><span class="social"><i></i><i></i><i></i><i></i></span></div>
    <nav class="nav">
      <a class="active" href="#">Home</a><a href="#">About Us</a><a href="#">Bootcamp</a>
      <span class="brand"><i></i>Pulse Forge</span>
      <a href="#">Photo Gallery</a><a href="#">Gym</a><a href="#">Contact</a>
    </nav>
  </header>

  <span class="slide-arrow" style="left:90px">&lsaquo;</span>
  <span class="slide-arrow" style="right:90px">&rsaquo;</span>
  <h1 class="hero-title">Pulse Forge Fitness</h1>
  <p class="hero-text">Train hard with a group that pushes you further. Indoor functional classes and outdoor bootcamps built to make you stronger every single week of the year.</p>
  <a class="btn center-x" style="top:380px">Read More</a>

  <!-- welcome -->
  <svg class="abs" style="left:576px;top:676px" width="48" height="48" viewBox="0 0 48 48" aria-hidden="true">
    <g fill="none" stroke="#1b1b1b" stroke-width="2.5">
      <line x1="4" y1="24" x2="44" y2="24"/><rect x="8" y="16" width="6" height="16"/><rect x="34" y="16" width="6" height="16"/>
      <circle cx="24" cy="10" r="5"/><line x1="24" y1="15" x2="24" y2="40"/><line x1="24" y1="40" x2="16" y2="46"/><line x1="24" y1="40" x2="32" y2="46"/>
    </g>
  </svg>
  <p class="eyebrow" style="top:772px">Welcome to</p>
  <h2 class="heading" style="top:800px">Pulse Forge Fitness</h2>
  <p class="para" style="left:240px;top:858px;width:720px;text-align:center">Our coaches run small group sessions that mix strength, conditioning and mobility so every member gets real attention. Whether you are starting out or chasing a new personal best, we build a plan around you and help you stay consistent, motivated and safe from your first class onward, indoors or out.</p>
  <a class="btn center-x" style="top:960px">Learn More</a>

  <!-- bootcamp -->
  <div class="abs" style="left:0;top:1060px;width:1200px;height:600px;background:var(--white)"></div>
  <div class="photo" style="left:740px;top:1020px;width:360px;height:640px;background:linear-gradient(180deg,#f1f1f1,#d9d9d9)" role="img" aria-label="Woman holding a handstand against a white brick wall"></div>
  <svg class="shapes" style="top:1060px" width="1200" height="600" viewBox="0 0 1200 600" aria-hidden="true">
    <polygon points="1000,260 1200,120 1200,520" fill="#fbed22"/>
  </svg>
  <div class="photo" style="left:0;top:1480px;width:620px;height:220px;background:linear-gradient(180deg,#3a3a3a,#0f0f0f)" role="img" aria-label="Rows of black medicine balls on a gym floor"></div>

  <p class="abs boot-kicker">Online</p>
  <h2 class="abs boot-title">Bootcamp</h2>
  <p class="abs boot-lead">Learn step by step how to get lean, eat clean and be more body confident!</p>
  <ul class="boot-list">
    <li><svg width="14" height="14" viewBox="0 0 14 14"><path d="M1 7l4 4 8-9" fill="none" stroke="#0692cd" stroke-width="2.5"/></svg>Step-by-step whole body plan in 4 weeks</li>
    <li><svg width="14" height="14" viewBox="0 0 14 14"><path d="M1 7l4 4 8-9" fill="none" stroke="#0692cd" stroke-width="2.5"/></svg>Weekly HD video workouts</li>
    <li><svg width="14" height="14" viewBox="0 0 14 14"><path d="M1 7l4 4 8-9" fill="none" stroke="#0692cd" stroke-width="2.5"/></svg>Home and gym workouts included</li>
    <li><svg width="14" height="14" viewBox="0 0 14 14"><path d="M1 7l4 4 8-9" fill="none" stroke="#0692cd" stroke-width="2.5"/></svg>Clean eating guide with easy to prepare meal plans, vegan and gluten free options</li>
    <li><svg width="14" height="14" viewBox="0 0 14 14"><path d="M1 7l4 4 8-9" fill="none" stroke="#0692cd" stroke-width="2.5"/></svg>Full online support</li>
    <li><svg width="14" height="14" viewBox="0 0 14 14"><path d="M1 7l4 4 8-9" fill="none" stroke="#0692cd" stroke-width="2.5"/></svg>Lifetime access</li>
  </ul>
  <div class="price"><span class="label">From only<br>payment of</span><span class="amount">$69.90</span></div>
  <a class="btn" style="left:240px;top:1548px;width:180px;background:var(--yellow)">Get Started Today</a>

  <!-- gallery heading -->
  <svg class="shapes" style="top:1640px" width="1200" height="212" viewBox="0 0 1200 212" aria-hidden="true">
    <polygon points="0,60 600,0 1200,60 1200,212 0,212" fill="#ffffff"/>
    <polygon points="0,0 0,60 600,0" fill="#ffffff"/>
    <polygon points="0,150 260,212 0,212" fill="#1b1b1b"/>
    <polygon points="1200,150 940,212 1200,212" fill="#1b1b1b"/>
  </svg>
  <svg class="abs" style="left:580px;top:1656px" width="40" height="46" viewBox="0 0 40 46" aria-hidden="true">
    <g fill="none" stroke="#1b1b1b" stroke-width="2.5"><circle cx="20" cy="26" r="16"/><line x1="20" y1="26" x2="20" y2="16"/><line x1="16" y1="4" x2="24" y2="4"/><line x1="20" y1="4" x2="20" y2="10"/></g>
  </svg>
  <p class="eyebrow" style="top:1724px">Photo Gallery</p>
  <h2 class="heading" style="top:1752px">Lorem Ipsum Is Simply</h2>

  <div class="gallery">
    <div role="img" aria-label="Group doing box jumps" style="background:linear-gradient(135deg,#8a6a55,#3b2f2a)"></div>
    <div role="img" aria-label="Athletes lifting kettlebells" style="background:linear-gradient(135deg,#4a6a86,#1f2d3a)"></div>
    <div role="img" aria-label="Rope climb in the gym" style="background:linear-gradient(135deg,#9a5a45,#3a2a24)"></div>
    <div role="img" aria-label="Couple stretching together" style="background:linear-gradient(135deg,#dcdcdc,#9a9a9a)"></div>
    <div role="img" aria-label="Woman training with dumbbells" style="background:linear-gradient(135deg,#e2d7d2,#a08a86)"></div>
    <div role="img" aria-label="Man doing push ups" style="background:linear-gradient(135deg,#355a78,#14212c)"></div>
    <div role="img" aria-label="Athlete with battle ropes" style="background:linear-gradient(135deg,#7d7a3a,#2a2a18)"></div>
    <div role="img" aria-label="Pull up rig workout" style="background:linear-gradient(135deg,#bdbdbd,#6f6f6f)"></div>
    <div role="img" aria-label="Group class with medicine balls" style="background:linear-gradient(135deg,#c9c0b8,#7a6f66)"></div>
    <div role="img" aria-label="Gymnastic rings training" style="background:linear-gradient(135deg,#cfcfcf,#565656)"></div>
  </div>

  <!-- band -->
  <svg class="shapes" style="top:2320px" width="1200" height="300" viewBox="0 0 1200 300" aria-hidden="true">
    <rect width="1200" height="300" fill="#1b1b1b"/>
    <polygon points="0,120 600,260 1200,120 1200,300 0,300" fill="#262626"/>
    <polygon points="0,0 360,0 0,110" fill="#222222"/>
    <polygon points="1200,0 840,0 1200,110" fill="#222222"/>
  </svg>
  <a class="btn center-x" style="top:2380px">Read More</a>

  <!-- videos -->
  <div class="photo" style="left:0;top:2600px;width:1200px;height:860px;background:linear-gradient(180deg,#262626,#151515)" role="img" aria-label="Dim gym interior background"></div>
  <h2 class="section-title-y" style="top:2626px">Videos</h2>
  <div class="video" role="img" aria-label="Video of an athlete training with battle ropes">
    <div class="tools"><i></i><i></i><i></i><i></i><i></i></div>
    <div class="bar"><span>&#9654;</span><div class="track"><span></span></div><span>HD</span><span>&#9633;</span></div>
  </div>

  <!-- gym -->
  <h2 class="section-title-y" style="top:3110px;font-size:26px">Gym</h2>
  <div class="gym-card" style="left:20px">
    <div class="photo-side" role="img" aria-label="Athlete lifting in the gym"></div>
    <h3>How Is Learn Gym</h3>
    <p>Our indoor functional classes combine strength circuits and cardio drills with expert coaching for every fitness level.</p>
  </div>
  <div class="gym-card" style="left:612px">
    <div class="photo-side" role="img" aria-label="Athlete flexing in the gym"></div>
    <h3>How Is Learn Gym</h3>
    <p>Outdoor bootcamp sessions run across the week in local parks, keeping workouts fresh, social and full of energy.</p>
  </div>

  <!-- blog -->
  <svg class="shapes" style="top:3420px" width="1200" height="1200" viewBox="0 0 1200 1200" aria-hidden="true">
    <polygon points="0,220 600,40 1200,220 1200,760 600,900 0,760" fill="#ffffff"/>
    <polygon points="0,760 600,900 0,1080" fill="#fbed22"/>
    <polygon points="1200,760 600,900 1200,1080" fill="#fbed22"/>
    <polygon points="0,1080 600,900 1200,1080 1200,1200 0,1200" fill="#1b1b1b"/>
  </svg>
  <svg class="abs" style="left:580px;top:3508px" width="40" height="40" viewBox="0 0 40 40" aria-hidden="true">
    <g fill="none" stroke="#1b1b1b" stroke-width="2.5"><rect x="3" y="7" width="34" height="30"/><line x1="3" y1="15" x2="37" y2="15"/><line x1="12" y1="3" x2="12" y2="10"/><line x1="28" y1="3" x2="28" y2="10"/></g>
  </svg>
  <p class="eyebrow" style="top:3584px">Blog</p>
  <h2 class="heading" style="top:3612px">Lorem Ipsum Is Simply</h2>

  <div class="blog-main" role="img" aria-label="Muscular man training with a barbell">
    <p class="caption">Build After Training The Right Way</p>
  </div>
  <div class="blog-small" style="left:612px;top:3700px" role="img" aria-label="Athlete resting after a set"><p>Eight tips for faster recovery</p></div>
  <div class="blog-small" style="left:792px;top:3700px" role="img" aria-label="Man lifting dumbbells"><p>Fuel your body before class</p></div>
  <div class="blog-small" style="left:612px;top:3920px" role="img" aria-label="Athlete doing kettlebell swings"><p>Why group training works</p></div>
  <div class="blog-small" style="left:792px;top:3920px" role="img" aria-label="Man training on a rig"><p>Your first bootcamp week</p></div>

  <!-- footer -->
  <div class="foot-brand"><i></i>Pulse Forge</div>
  <footer class="footer">
    <div class="col"><h4>About Us</h4><p>Pulse Forge Fitness runs small group gym and outdoor bootcamp classes for people who want real results and a friendly team around them.</p></div>
    <div class="col"><h4>Information</h4><ul><li>Home</li><li>About Us</li><li>Bootcamp</li><li>Photo Gallery</li><li>Gym</li></ul></div>
    <div class="col contact"><h4>Contact Us</h4><ul><li><i></i>+61 2 5550 0148</li><li><i></i>hello@pulseforge.example</li><li><i></i>12 Harbour Lane, Sydney</li><li><i></i>Mon–Sat 5am – 8pm</li></ul></div>
  </footer>
  <div class="copyright"><span>© Copyright 2024 Pulse Forge Fitness. All rights reserved.</span><span>pulseforge.example</span></div>
</div>
</body>
</html>
```